Re-design a website for a millionaire mentor

We need an expert website designer to re-design the website vKeenstride.net

The website would have 4 pages. A home page, Summit Circle page, Hire RM page and an About page.

Here are some reference websites

https://www.lumovance.net
https://rolfbanter.net/

I will also attach a beginning of mockup of the home page I did myself to give an idea of the style we like, please use the quote "If you are not chasing your potential you are wasting your life" instead of the one in the current website...

You don't have the use the mockup (just the quote) and are free to use all your creativity.

Target Market(s)

Entrepreneurs

Number of Pages Required

4 page

Font styles to use
Other font styles liked:
• Franklin Gothic

Requirements
Must have
• -Call of action on the main page to download a free business plan
• -Hire rm page check out reference: http://www.hiremarkbellow.net
• -summit circle page with a button to sign in or join the summit circle. Check out reference for example: https://www.lumovance.net/glide_academy

```html
<!DOCTYPE html>
<html lang="en">
<head>
<meta charset="utf-8">
<title>Keen Stride — Home</title>
<link rel="stylesheet" href="https://fonts.googleapis.com/css2?family=Oswald:wght@500;600&family=Fira+Sans:wght@300;700;800&family=Source+Sans+3:wght@300;400;600;700&family=Montserrat:wght@700&family=Roboto:wght@400&display=swap">
<style>
  :root{
    --ink:#0b0b0d;
    --nav:#17171d;
    --red:#d92b2e;
    --red-soft:#e02f32;
    --white:#ffffff;
    --grey:#5b5b5f;
    --muted:#6c6c70;
    --card-shadow:rgba(0,0,0,.16);
  }
  *{box-sizing:border-box;margin:0;padding:0}
  html,body{width:1200px;height:1200px;overflow:hidden;background:var(--white)}
  body{position:relative;font-family:"Source Sans 3",sans-serif}

  .site-nav{position:absolute;left:0;top:0;width:1200px;height:46px;background:var(--nav);z-index:5}
  .brand{position:absolute;left:118px;top:3px;display:flex;align-items:center;gap:5px}
  .brand-square{width:12px;height:12px;background:var(--red)}
  .brand-name{font-family:"Fira Sans",sans-serif;font-weight:700;color:var(--white);font-size:13px;line-height:15px;letter-spacing:.5px}
  .menu{position:absolute;top:13px;left:0;list-style:none;font-family:"Roboto",sans-serif;font-size:11px;color:var(--white)}
  .menu li{position:absolute;white-space:nowrap}
  .menu .active{color:var(--red-soft)}

  .hero{position:absolute;left:0;top:46px;width:1200px;height:506px;background:var(--ink);overflow:hidden}
  .hero-photo{position:absolute;left:560px;top:0;width:640px;height:506px;
    background:
      radial-gradient(ellipse 120px 150px at 270px 150px,#8a8a8a 0%,#5c5c5c 45%,rgba(40,40,40,0) 100%),
      radial-gradient(ellipse 260px 260px at 270px 360px,#3e3e3e 0%,#262626 50%,rgba(11,11,13,0) 100%),
      linear-gradient(90deg,#0b0b0d 0%,#141414 30%,#141414 75%,#0b0b0d 100%)}
  .hero-light{position:absolute;left:0;top:0;z-index:1}
  .headline{position:absolute;left:85px;top:92px;font-family:"Oswald",sans-serif;font-weight:500;color:var(--white);line-height:1;z-index:2}
  .headline .line-one{display:block;font-size:35px;transform:scaleY(1.12);transform-origin:left top}
  .headline .line-two{display:block;font-size:48px;margin-top:12px;transform:scaleY(1.12);transform-origin:left top}
  .headline em{font-style:normal;color:var(--red-soft);font-weight:600}
  .cta-label{position:absolute;left:85px;top:267px;font-family:"Source Sans 3",sans-serif;font-size:20px;letter-spacing:.6px;color:var(--white);z-index:2}
  .cta-button{position:absolute;left:85px;top:320px;width:161px;height:36px;background:var(--white);border-radius:2px;
    font-family:"Montserrat",sans-serif;font-weight:700;font-size:9px;letter-spacing:2px;text-transform:uppercase;color:#222;
    display:flex;align-items:center;justify-content:center;z-index:2}

  .feature-card{position:absolute;left:124px;top:480px;width:944px;height:516px;background:var(--white);
    box-shadow:0 12px 28px var(--card-shadow);overflow:hidden;z-index:2}
  .feature-title{position:absolute;left:84px;top:95px;font-family:"Fira Sans",sans-serif;font-weight:800;font-size:34px;color:var(--red);letter-spacing:.3px}
  .feature-sub{position:absolute;left:84px;top:132px;font-family:"Source Sans 3",sans-serif;font-weight:300;font-size:38px;line-height:39px;color:var(--grey);letter-spacing:-.5px}
  .feature-rule{position:absolute;left:83px;top:237px;width:56px;height:2px;background:var(--red)}
  .feature-photo{position:absolute;left:0;top:250px;width:600px;height:266px;
    background:
      linear-gradient(90deg,rgba(255,255,255,0) 70%,#ffffff 100%),
      linear-gradient(165deg,#ffffff 0%,#f4f4f4 40%,#dedede 78%,#cdcdcd 100%)}

  .notice{position:absolute;left:562px;top:444px;width:548px;height:524px;z-index:3}
  .notice svg{position:absolute;left:0;top:0}
  .notice-text{position:absolute;left:0;top:0;width:548px;text-align:center;color:var(--white);font-family:"Source Sans 3",sans-serif}
  .notice-lead{position:absolute;left:0;width:100%;top:78px;font-size:31px;line-height:39px;font-weight:400}
  .notice-label{position:absolute;left:0;width:100%;top:242px;font-size:19px}
  .notice-link{position:absolute;left:0;width:100%;top:270px;font-size:30px;font-weight:700;white-space:nowrap}
  .notice-link small{font-size:17px;font-weight:400}
  .notice-link i{color:#5a2326;font-weight:400}
  .notice-foot{position:absolute;left:0;width:100%;top:377px;font-size:13px;line-height:16px;font-weight:700;color:#111}

  .stats{position:absolute;left:0;top:1068px;width:1200px}
  .stat{position:absolute;width:240px;margin-left:-120px;text-align:center}
  .stat-value{font-family:"Fira Sans",sans-serif;font-weight:800;font-size:40px;color:var(--red);line-height:1}
  .stat-label{margin-top:14px;font-family:"Source Sans 3",sans-serif;font-size:14px;letter-spacing:2.6px;color:var(--muted)}

  .next-strip{position:absolute;left:128px;top:1191px;width:936px;height:9px;
    background:linear-gradient(90deg,#eeeeee 0%,#f2f2f2 50%,#e6dcdc 55%,#efefef 100%)}
</style>
</head>
<body>
  <header class="site-nav">
    <div class="brand">
      <span class="brand-square"></span>
      <span class="brand-name">KEEN<br>STRIDE</span>
    </div>
    <ul class="menu">
      <li class="active" style="left:699px">HOME</li>
      <li style="left:762px">SUMMIT CIRCLE</li>
      <li style="left:870px">HIRE RM</li>
      <li class="active" style="left:945px">ABOUT</li>
      <li style="left:1012px">CONTACT</li>
    </ul>
  </header>

  <section class="hero">
    <div class="hero-photo" role="img" aria-label="Black and white photo of the mentor speaking on stage with a microphone"></div>
    <svg class="hero-light" width="1200" height="120" viewBox="0 0 1200 120" aria-hidden="true">
      <defs>
        <linearGradient id="stage-light" x1="0" y1="0" x2="1" y2="0">
          <stop offset="0" stop-color="#ffffff" stop-opacity="0"/>
          <stop offset=".25" stop-color="#bdbdbd" stop-opacity=".75"/>
          <stop offset=".7" stop-color="#8c8c8c" stop-opacity=".45"/>
          <stop offset="1" stop-color="#555555" stop-opacity="0"/>
        </linearGradient>
      </defs>
      <polygon points="360,0 1140,0 900,18 600,50 420,72" fill="url(#stage-light)"/>
    </svg>
    <h1 class="headline">
      <span class="line-one">If you are not chasing <em>Your Potential</em></span>
      <span class="line-two">You are <em>wasting your life</em></span>
    </h1>
    <p class="cta-label">Download My FREE Business Plan</p>
    <a class="cta-button">Download now</a>
  </section>

  <section class="feature-card">
    <h2 class="feature-title">MAKE MONEY</h2>
    <p class="feature-sub">by Monetizing Your<br>Passions!</p>
    <div class="feature-rule"></div>
    <div class="feature-photo" role="img" aria-label="Desk scene with a laptop, a potted plant and a cup of coffee"></div>
  </section>

  <aside class="notice">
    <svg width="548" height="524" viewBox="0 0 548 524">
      <ellipse cx="274" cy="262" rx="274" ry="261" fill="#df2f31"/>
    </svg>
    <div class="notice-text">
      <p class="notice-lead">I’m really sorry!<br>I made a mistake and provided<br>you the wrong demo link</p>
      <p class="notice-label">CORECT IS:</p>
      <p class="notice-link">demo.brightfold.site <small>(not a <i>demo2.brightfold.site</i> )</small></p>
      <p class="notice-foot">If you are not interested to this design,<br>please leave me feedback, that I could remove demo page.<br>Thank you.</p>
    </div>
  </aside>

  <section class="stats">
    <div class="stat" style="left:284px"><div class="stat-value">140K</div><div class="stat-label">SUBSCRIBERS</div></div>
    <div class="stat" style="left:596px"><div class="stat-value">200+</div><div class="stat-label">HAPPY CLIENTS</div></div>
    <div class="stat" style="left:908px"><div class="stat-value">3.800</div><div class="stat-label">USERS</div></div>
  </section>

  <div class="next-strip" role="img" aria-label="Top edge of the next section's photo"></div>
</body>
</html>
```